Create a Eye Catching Web Design

We need an informative web design that needs to be eye catching and unique. All of the information needs to be on that page - We have a shopfront setup in the next 2 weeks so the website needs to be ready asap. We are selling mainly rehabilitation aids and mobility products.

The website is main purpose is to inform customers about our range of products, address and phone number. This is an interim website until we get an ecommerce website setup. We are not looking for an ecommerce website, just simple, eye-catching and informative. clean, crisp and modern -target age 45-75 yo (men and women)

I have included our logo and brochure designed with our range of product categories.

The website needs to be designed, coded and setup completely as a finished product.

As soon as the website design is chosen, the chosen designer would need to get the website up and running. If the website design is chosen and great, we could use the same designer for the ecommerce build as well.

www.velnorcare.com
www.velnorcare.com.au
Updates

Project Deadline Extended
Reason: I haven't received as many designs but variations from the same designers.

Target Market(s)

45-75

Industry/Entity Type

Health And Wellness

Coding

Coded - Design and coding required

Number of Pages Required

2 page

Font styles to use
Sans Serif

Requirements
Nice to have
• clean design, modern feel - not cluttered - something unique. for the market age

```html
<!DOCTYPE html>
<html lang="en">
<head>
<meta charset="utf-8">
<title>Velnor Care</title>
<link href="https://fonts.googleapis.com/css2?family=Roboto:wght@300;400;500;700&family=Roboto+Slab:wght@300;400&display=swap" rel="stylesheet">
<style>
:root{
  --red:#e8202a;
  --green:#34c21d;
  --dark:#3a3a3a;
  --darker:#2a2a2a;
  --text:#333;
  --beige:#f2ebdd;
  --white:#fff;
}
*{margin:0;padding:0;box-sizing:border-box}
html,body{width:1200px;height:3249px;overflow:hidden}
body{position:relative;font-family:'Roboto',sans-serif;color:var(--text);background:var(--white)}
.abs{position:absolute}
a{color:inherit;text-decoration:none}

/* header */
.site-header{position:absolute;left:0;top:0;width:1200px;height:108px;background:var(--white)}
.brand{left:80px;top:26px;display:flex;align-items:center;gap:12px;font-size:34px;font-weight:700;color:var(--red);letter-spacing:1px}
.brand-dot{width:26px;height:26px;border-radius:50%;background:var(--red)}
.top-contact{right:80px;top:18px;display:flex;gap:28px;font-size:15px;color:#444}
.top-contact b{font-size:18px;font-weight:700}
.top-contact span{display:flex;align-items:center;gap:8px}
.main-nav{right:80px;top:66px;display:flex;gap:22px;font-size:13.5px;text-transform:uppercase;color:#333}
.main-nav .active{color:var(--red)}

/* hero */
.hero{left:0;top:108px;width:1200px;height:589px;background:
  radial-gradient(ellipse 260px 320px at 700px 300px,rgba(225,232,240,.75) 0%,rgba(225,232,240,0) 100%),
  linear-gradient(100deg,#2f8a2c 0%,#4f9e36 30%,#86bd5a 52%,#b9d88f 70%,#8cbc56 85%,#5e9a34 100%)}
.hero-title{left:80px;top:244px;font-size:40px;font-weight:400;color:var(--white);line-height:50px;text-transform:uppercase}
.hero-text{left:80px;top:372px;width:520px;font-size:15.5px;line-height:25px;color:var(--white)}
.btn-red{left:80px;top:480px;width:220px;height:42px;border-radius:21px;background:var(--red);color:var(--white);font-size:14.5px;text-transform:uppercase;display:flex;align-items:center;justify-content:center}

/* categories */
.cat-tabs{left:80px;top:672px;width:1040px;height:69px;display:flex}
.cat-tab{flex:1;display:flex;align-items:center;justify-content:center;text-align:center;color:var(--white);font-size:15px;line-height:21px;text-transform:uppercase}
.cat-tab.red{background:var(--red)}
.cat-tab.green{background:var(--green)}
.cat-icons{left:80px;top:750px;width:1040px;height:170px;display:flex}
.cat-icon{flex:1;display:flex;flex-direction:column;align-items:center}
.cat-icon .dots{width:6px;height:78px;background:radial-gradient(circle,currentColor 2.8px,transparent 3px) 0 0/6px 13px repeat-y}
.red-c{color:var(--red)}
.green-c{color:var(--green)}

/* section headings */
.section-title{left:0;width:1200px;text-align:center;font-family:'Roboto Slab',serif;font-weight:300;font-size:31px;color:#222;text-transform:uppercase}
.title-rule{left:576px;width:48px;height:3px;background:var(--red)}

/* products */
.product{top:1111px;width:240px}
.product-photo{width:240px;height:271px;background:var(--beige);padding:12px}
.product-photo div{width:100%;height:100%;border:2px solid var(--red)}
.product-name{margin-top:16px;text-align:center;color:var(--red);font-size:21px;font-weight:500}
.btn-green{margin:14px auto 0;width:121px;height:35px;border-radius:18px;background:var(--green);color:var(--white);font-size:13px;display:flex;align-items:center;justify-content:center}
.slider-arrow{top:1224px}

/* stories */
.stories{left:0;top:1538px;width:1200px;height:446px;background:var(--red)}
.story-photo{left:80px;top:1616px;width:286px;height:286px;border-radius:50%;background:radial-gradient(circle at 45% 40%,#f4efe9 0%,#c9d3da 45%,#7f98a8 80%,#55697a 100%);border:4px solid rgba(255,255,255,.6)}
.story-kicker{left:435px;top:1610px;font-size:15px;text-transform:uppercase;color:var(--white)}
.story-title{left:435px;top:1628px;font-size:32px;font-weight:700;color:var(--white)}
.story-text{left:435px;top:1676px;width:425px;font-size:15px;line-height:23px;color:var(--white)}
.btn-white{left:435px;top:1882px;width:117px;height:36px;border-radius:18px;background:var(--white);color:var(--red);font-size:13px;display:flex;align-items:center;justify-content:center}
.story-divider{left:873px;top:1636px;width:1px;height:238px;background:rgba(255,255,255,.6)}
.other-stories{left:901px;top:1650px;font-size:15px;color:var(--white)}
.other-stories h4{font-weight:500;font-size:15px;text-transform:uppercase;margin-bottom:14px}
.other-stories li{list-style:none;line-height:32px;display:flex;align-items:center;gap:8px}
.other-stories li::before{content:"";border-left:7px solid var(--white);border-top:5px solid transparent;border-bottom:5px solid transparent}

/* map */
.map{left:0;top:1984px;width:1200px;height:373px;background:linear-gradient(160deg,#e9ece4 0%,#e4e7de 50%,#dde3d6 100%)}
.map-card{left:617px;top:2097px;width:239px;height:87px;background:var(--white);border:1px solid #bbb;padding:12px 16px;font-size:13.5px;line-height:21px;color:#333}
.map-card div{display:flex;align-items:center;gap:8px}

/* gallery */
.lives{top:2552px;width:300px;height:260px}

/* footer */
.footer{left:0;top:2877px;width:1200px;height:316px;background:linear-gradient(90deg,#3a3a3a 0%,#3e3e3e 60%,#474747 100%)}
.footer-heading{position:absolute;top:2943px;font-size:18px;font-weight:400;color:var(--white);text-transform:uppercase;padding-bottom:10px;border-bottom:1px solid #5a5a5a}
.contact-list{left:80px;top:2992px;font-size:16px;color:var(--white)}
.contact-list div{display:flex;align-items:center;gap:14px;height:37px}
.socials{left:80px;top:3109px;display:flex;gap:14px}
.socials span{width:22px;height:22px;border-radius:50%;background:var(--red)}
.about-text{left:435px;top:2992px;width:380px;font-size:13px;line-height:21px;color:#e4e4e4}
.about-text p{margin-bottom:14px}
.quick-links{left:932px;top:2990px;font-size:13px;line-height:23px;color:#eee;list-style:none}
.bottom-bar{left:0;top:3193px;width:1200px;height:56px;background:var(--darker)}
.copyright{left:80px;top:3214px;font-size:11px;color:#aaa}
.accept{left:850px;top:3208px;display:flex;align-items:center;gap:8px;font-size:11px;color:#ccc}
.accept span{width:44px;height:26px;border-radius:3px;background:#e8e8e8}
</style>
</head>
<body>

<header class="site-header">
  <div class="abs brand"><span>Velnor Care</span><span class="brand-dot"></span></div>
  <div class="abs top-contact">
    <span><svg width="16" height="16" viewBox="0 0 24 24"><path fill="#e8202a" d="M6.6 10.8a15 15 0 0 0 6.6 6.6l2.2-2.2c.3-.3.7-.4 1-.2 1.1.4 2.3.6 3.6.6.6 0 1 .4 1 1V20c0 .6-.4 1-1 1A17 17 0 0 1 3 4c0-.6.4-1 1-1h3.5c.6 0 1 .4 1 1 0 1.3.2 2.5.6 3.6.1.3 0 .7-.2 1z"/></svg><b>68451230</b></span>
    <span><svg width="14" height="18" viewBox="0 0 24 30"><path fill="#e8202a" d="M12 0a10 10 0 0 0-10 10c0 8 10 20 10 20s10-12 10-20A10 10 0 0 0 12 0zm0 14a4 4 0 1 1 0-8 4 4 0 0 1 0 8z"/></svg>14 Brinley st, Ashford</span>
  </div>
  <nav class="abs main-nav">
    <a class="active">Home</a><a>About Us</a><a>Our Products</a><a>What's New</a><a>Gallery</a><a>Find a Reseller</a><a>Contact Us</a>
  </nav>
</header>

<section class="abs hero" role="img" aria-label="Photo of a smiling carer with an elderly woman in a wheelchair on a leafy park path"></section>
<h1 class="abs hero-title">Quality products for<br>a better quality of life.</h1>
<p class="abs hero-text">Velnor Care Offers a Wide Range Of Mobility &amp; Rehab Products Including High End Massage Chairs, Electric Scooters, Wheelchairs, Walkers &amp; Daily Living Aids.</p>
<a class="abs btn-red">See our products</a>

<div class="abs cat-tabs">
  <div class="cat-tab red">Massage<br>Recliners</div>
  <div class="cat-tab green">Electric<br>Scooters</div>
  <div class="cat-tab red">Walking<br>Aids</div>
  <div class="cat-tab green">Everyday Living<br>Aids</div>
  <div class="cat-tab red">Consumer<br>Health</div>
  <div class="cat-tab green">Wound Care<br>Products</div>
</div>
<div class="abs cat-icons">
  <div class="cat-icon red-c"><span class="dots"></span><svg width="94" height="86" viewBox="0 0 100 90"><path fill="currentColor" d="M50 88 8 46C-4 34-1 12 16 6c12-4 25 1 34 12C59 7 72 2 84 6c17 6 20 28 8 40z"/><rect x="36" y="36" width="28" height="8" rx="4" fill="#fff"/><rect x="34" y="30" width="8" height="24" rx="4" fill="#fff"/></svg></div>
  <div class="cat-icon green-c"><span class="dots"></span><svg width="94" height="86" viewBox="0 0 100 90"><path fill="currentColor" d="M50 88 8 46C-4 34-1 12 16 6c12-4 25 1 34 12C59 7 72 2 84 6c17 6 20 28 8 40z"/><circle cx="40" cy="56" r="5" fill="#fff"/><circle cx="62" cy="56" r="5" fill="#fff"/><path d="M36 48h28l-6-18h-6" stroke="#fff" stroke-width="4" fill="none"/></svg></div>
  <div class="cat-icon red-c"><span class="dots"></span><svg width="94" height="86" viewBox="0 0 100 90"><path fill="currentColor" d="M50 88 8 46C-4 34-1 12 16 6c12-4 25 1 34 12C59 7 72 2 84 6c17 6 20 28 8 40z"/><path d="M38 62V30h24v32M38 42h24" stroke="#fff" stroke-width="4" fill="none"/></svg></div>
  <div class="cat-icon green-c"><span class="dots"></span><svg width="94" height="86" viewBox="0 0 100 90"><path fill="currentColor" d="M50 88 8 46C-4 34-1 12 16 6c12-4 25 1 34 12C59 7 72 2 84 6c17 6 20 28 8 40z"/><circle cx="46" cy="28" r="4" fill="#fff"/><path d="M46 34v14h12l4 10M42 42a12 12 0 1 0 14 16" stroke="#fff" stroke-width="4" fill="none"/></svg></div>
  <div class="cat-icon red-c"><span class="dots"></span><svg width="94" height="86" viewBox="0 0 100 90"><path fill="currentColor" d="M50 88 8 46C-4 34-1 12 16 6c12-4 25 1 34 12C59 7 72 2 84 6c17 6 20 28 8 40z"/><path d="M28 44h12l5-10 8 20 5-10h14" stroke="#fff" stroke-width="4" fill="none"/></svg></div>
  <div class="cat-icon green-c"><span class="dots"></span><svg width="94" height="86" viewBox="0 0 100 90"><path fill="currentColor" d="M50 88 8 46C-4 34-1 12 16 6c12-4 25 1 34 12C59 7 72 2 84 6c17 6 20 28 8 40z"/><rect x="34" y="36" width="32" height="14" rx="7" fill="#fff" transform="rotate(45 50 43)"/><rect x="34" y="36" width="32" height="14" rx="7" fill="#fff" transform="rotate(-45 50 43)"/></svg></div>
</div>

<h2 class="abs section-title" style="top:993px">Our Products</h2>
<div class="abs title-rule" style="top:1040px"></div>

<svg class="abs slider-arrow" style="left:32px" width="30" height="50" viewBox="0 0 30 50"><path d="M26 4 6 25l20 21" stroke="#777" stroke-width="2" fill="none"/></svg>
<svg class="abs slider-arrow" style="left:1140px" width="30" height="50" viewBox="0 0 30 50"><path d="M4 4l20 21L4 46" stroke="#777" stroke-width="2" fill="none"/></svg>

<article class="abs product" style="left:80px"><div class="product-photo"><div role="img" aria-label="Product photo of a red and white massage recliner" style="background:radial-gradient(ellipse 45% 40% at 50% 55%,#c8485a 0%,#e0b8b8 55%,#f2ebdd 100%)"></div></div><h3 class="product-name">Massgae Recliners</h3><a class="btn-green">VIEW MORE</a></article>
<article class="abs product" style="left:347px"><div class="product-photo"><div role="img" aria-label="Product photo of a covered electric mobility scooter" style="background:radial-gradient(ellipse 45% 40% at 50% 52%,#4a4a4a 0%,#b8b4ae 55%,#f2ebdd 100%)"></div></div><h3 class="product-name">Electric Scooters</h3><a class="btn-green">VIEW MORE</a></article>
<article class="abs product" style="left:615px"><div class="product-photo"><div role="img" aria-label="Product photo of a folding wheelchair" style="background:radial-gradient(ellipse 45% 40% at 50% 55%,#555 0%,#bdb8b0 55%,#f2ebdd 100%)"></div></div><h3 class="product-name">walking Aids</h3><a class="btn-green">VIEW MORE</a></article>
<article class="abs product" style="left:880px"><div class="product-photo"><div role="img" aria-label="Product photo of a commode chair, walking stick and shower stool" style="background:radial-gradient(ellipse 45% 40% at 50% 55%,#9a9a9a 0%,#d8d2c8 55%,#f2ebdd 100%)"></div></div><h3 class="product-name">Everyday Living Aids</h3><a class="btn-green">VIEW MORE</a></article>

<section class="abs stories"></section>
<div class="abs story-photo" role="img" aria-label="Circular photo of a smiling woman working at a desk"></div>
<div class="abs story-kicker">In our own words</div>
<h2 class="abs story-title">Lumara Stories</h2>
<p class="abs story-text">Lorem ipsum dolor sit amet, consectetur adipiscing elit. Sed scelerisque nisi ornare nisi lacinia, sollicitudin commodo massa tempor. Aliquam at eleifend lacus, vitae sollicitudin enim. Suspendisse tempor lorem sed ipsum maximus viverra. Maecenas justo mauris, viverra ut felis sed, finibus semper turpis. Phasellus eu ex diam. Vestibulum maximus libero et luctus tempor.</p>
<a class="abs btn-white">VIEW MORE</a>
<div class="abs story-divider"></div>
<div class="abs other-stories">
  <h4>Other stories</h4>
  <ul>
    <li>Lorem ipsum dolor sit</li>
    <li>Consectetur adipiscing</li>
    <li>Sed scelerisque</li>
    <li>Sollicitudin commodo</li>
    <li>Massa tempor</li>
    <li>Aliquam at eleifend</li>
  </ul>
</div>

<section class="abs map" role="img" aria-label="Street map of the town showing the store location"></section>
<div class="abs map-card">
  <div><svg width="11" height="14" viewBox="0 0 24 30"><path fill="#e8202a" d="M12 0a10 10 0 0 0-10 10c0 8 10 20 10 20s10-12 10-20A10 10 0 0 0 12 0z"/></svg>14 Brinley st, Ashford</div>
  <div><svg width="12" height="12" viewBox="0 0 24 24"><path fill="#e8202a" d="M6.6 10.8a15 15 0 0 0 6.6 6.6l2.2-2.2c.3-.3.7-.4 1-.2 1.1.4 2.3.6 3.6.6.6 0 1 .4 1 1V20c0 .6-.4 1-1 1A17 17 0 0 1 3 4c0-.6.4-1 1-1h3.5c.6 0 1 .4 1 1 0 1.3.2 2.5.6 3.6.1.3 0 .7-.2 1z"/></svg><b>68451230</b></div>
  <div style="font-size:12px"><svg width="12" height="9" viewBox="0 0 24 18"><rect width="24" height="18" rx="2" fill="#e8202a"/></svg>contact@velnorcare.com</div>
</div>
<svg class="abs" style="left:650px;top:2196px" width="22" height="30" viewBox="0 0 24 30"><path fill="#d9822b" d="M12 0a10 10 0 0 0-10 10c0 8 10 20 10 20s10-12 10-20A10 10 0 0 0 12 0zm0 14a4 4 0 1 1 0-8 4 4 0 0 1 0 8z"/></svg>

<h2 class="abs section-title" style="top:2442px">Our quality products changed peoples’ lives</h2>
<div class="abs title-rule" style="top:2489px"></div>

<div class="abs lives" style="left:0;background:linear-gradient(180deg,#4f7f3a 0%,#8a7a5a 35%,#b46a45 60%,#c0673e 100%)" role="img" aria-label="Photo of a tennis player in a sports wheelchair on a clay court"></div>
<div class="abs lives" style="left:300px;background:linear-gradient(180deg,#5f8b4a 0%,#7a8d60 45%,#8e4a44 70%,#6a7a52 100%)" role="img" aria-label="Photo of a man riding a red mobility scooter outdoors"></div>
<div class="abs lives" style="left:600px;background:linear-gradient(180deg,#a9c08d 0%,#88a878 45%,#c9a7b5 75%,#9aaa8a 100%)" role="img" aria-label="Photo of a carer with an elderly woman using a walker in a garden"></div>
<div class="abs lives" style="left:900px;background:linear-gradient(180deg,#2a2a2a 0%,#4a3a32 55%,#6a4a3a 100%)" role="img" aria-label="Photo of a woman relaxing in a dark massage chair"></div>

<footer class="abs footer"></footer>
<h3 class="footer-heading" style="left:80px;width:320px">Contact Information</h3>
<h3 class="footer-heading" style="left:435px;width:380px">About Us</h3>
<h3 class="footer-heading" style="left:932px;width:188px">Quick Links</h3>
<div class="abs contact-list">
  <div><svg width="12" height="16" viewBox="0 0 24 30"><path fill="#fff" d="M12 0a10 10 0 0 0-10 10c0 8 10 20 10 20s10-12 10-20A10 10 0 0 0 12 0zm0 14a4 4 0 1 1 0-8 4 4 0 0 1 0 8z"/></svg>14 Brinley st, Ashford</div>
  <div><svg width="14" height="14" viewBox="0 0 24 24"><path fill="#fff" d="M6.6 10.8a15 15 0 0 0 6.6 6.6l2.2-2.2c.3-.3.7-.4 1-.2 1.1.4 2.3.6 3.6.6.6 0 1 .4 1 1V20c0 .6-.4 1-1 1A17 17 0 0 1 3 4c0-.6.4-1 1-1h3.5c.6 0 1 .4 1 1 0 1.3.2 2.5.6 3.6.1.3 0 .7-.2 1z"/></svg>68451230</div>
  <div style="font-size:13px"><svg width="16" height="16" viewBox="0 0 24 24"><circle cx="12" cy="12" r="10" fill="none" stroke="#fff" stroke-width="2"/><path d="M2 12h20M12 2c4 4 4 16 0 20M12 2c-4 4-4 16 0 20" stroke="#fff" stroke-width="1.5" fill="none"/></svg>www.velnorcare.com</div>
</div>
<div class="abs socials"><span></span><span></span><span></span><span></span></div>
<div class="abs about-text">
  <p>Suspendisse nec ligula eget libero pulvinar pretium. Phasellus arcu dolor, tempus vitae luctus nec, eleifend ac purus.</p>
  <p>Proin dapibus justo lacus, a cursus nisi semper vitae. Sed aliquet augue lorem, nec sollicitudin quam hendrerit eu.</p>
</div>
<ul class="abs quick-links">
  <li>HOME</li><li>ABOUT US</li><li>OUR PRODUCTS</li><li>WHAT'S NEW</li><li>GALLERY</li><li>FIND A RESELLER</li><li>CONTACT US</li>
</ul>
<div class="abs bottom-bar"></div>
<div class="abs copyright">COPYRIGHT@VELNORCARE.COM. ALL RIGHTS ARE RESERVED.</div>
<div class="abs accept">WE ACCEPT: <span></span><span></span><span></span><span></span></div>

</body>
</html>
```